Verpackung für Hanf-Nudeln gesucht
Zielgruppe
Wir haben Hanf & Natur Shops und Onlineshop. Zielgruppe sind Menschen die gesund und bewusst Leben möchten.
Aufgabenstellung
Verpackung für Hanf-Nudeln (Suppen-, Band-, Spaghetti-, Hörnchennudeln). 500g abgepackt.
Wichtig: handgemacht in Österreich, 100 % vegan und bio
sie enthalten Dinkel- und Hanfmehl sowie geringe Mengen an Selvin KRISTALLSALZ und werden mit nitratfreiem Wasser erzeugt. Die Hanfnudeln sind vollkommen frei von synthetischen Hilfsmitteln. Kochzeit ca. 3 Minuten., Info für alle Allergiker, Hanfnudeln sind NICHT GLUTENFREI., Zutaten: Dinkel, Hanfmehl, Steinsalz, nitratfreies Wasser
Verpackungsvorschläge bitte
Modernes Design, passend zu unseren anderen Tirovelmo Produkten

```html
<!DOCTYPE html>
<html lang="de">
<head>
<meta charset="utf-8">
<title>Tirovelmo Hanfnudeln – Verpackung</title>
<link rel="stylesheet" href="https://fonts.googleapis.com/css2?family=Montserrat:wght@600&family=Open+Sans:wght@400;600;700&family=Caveat+Brush&display=swap">
<style>
  :root {
    --kraft: #b68a64;
    --kraft-light: #c7a080;
    --band: #c9a485;
    --label-white: #f3f1ee;
    --veil: rgba(235, 228, 220, 0.45);
    --leaf-dark: #1f4722;
    --leaf-mid: #3d6f34;
    --leaf-light: #5b8c48;
    --brand-green: #2f6b3a;
    --ink: #222;
    --title-brown: #4a3a30;
    --white: #ffffff;
  }
  * { margin: 0; padding: 0; box-sizing: border-box; }
  html, body { width: 896px; height: 1200px; overflow: hidden; }
  body {
    position: relative;
    background: linear-gradient(100deg, var(--kraft) 0%, var(--kraft-light) 50%, var(--kraft) 100%);
    font-family: "Open Sans", sans-serif;
  }
  .leaf-photo {
    position: absolute;
    left: 195px;
    width: 512px;
  }
  .leaf-photo--top {
    top: 224px; height: 329px;
    background: linear-gradient(135deg, var(--leaf-dark) 0%, var(--leaf-mid) 45%, var(--leaf-light) 70%, var(--leaf-dark) 100%);
  }
  .leaf-photo--bottom {
    top: 937px; height: 263px;
    background: linear-gradient(160deg, var(--leaf-mid) 0%, var(--leaf-dark) 40%, var(--leaf-light) 75%, var(--leaf-dark) 100%);
  }
  .brand-box {
    position: absolute;
    left: 269px; top: 0;
    width: 358px; height: 324px;
    background: var(--white);
    display: flex; flex-direction: column; align-items: center; justify-content: center; gap: 22px;
  }
  .brand-dot {
    width: 70px; height: 70px; border-radius: 50%;
    background: var(--brand-green);
    margin-top: 40px;
  }
  .brand-name {
    font-family: "Montserrat", sans-serif;
    font-weight: 600;
    font-size: 32px;
    letter-spacing: 1px;
    color: var(--ink);
  }
  .claim-band {
    position: absolute;
    left: 195px; width: 512px;
    background: var(--band);
    color: var(--white);
    font-weight: 600;
    font-size: 23px;
    text-align: center;
  }
  .claim-band--origin { top: 553px; height: 43px; line-height: 43px; }
  .claim-band--diet { top: 890px; height: 47px; line-height: 47px; font-weight: 700; letter-spacing: 0.5px; }
  .veil-band {
    position: absolute;
    left: 90px; top: 596px; width: 729px; height: 288px;
    background: var(--veil);
  }
  .product-label {
    position: absolute;
    left: 195px; top: 596px; width: 512px; height: 294px;
    background: var(--label-white);
  }
  .product-title {
    position: absolute;
    left: 50px; top: 12px;
    font-family: "Caveat Brush", cursive;
    color: var(--title-brown);
    font-size: 108px;
    line-height: 78px;
  }
  .product-title span { display: block; }
  .product-title .line-2 { margin-left: 38px; }
  .ingredients {
    position: absolute;
    left: 0; right: 0; top: 178px;
    text-align: center;
    font-size: 17px;
    line-height: 22px;
    color: var(--ink);
  }
  .ingredients strong { color: #1f3d22; font-weight: 700; }
  .pack-info {
    position: absolute;
    right: 8px; bottom: 6px;
    display: flex; align-items: flex-end; gap: 4px;
    font-size: 15px; color: var(--ink);
  }
</style>
</head>
<body>
  <div class="leaf-photo leaf-photo--top" role="img" aria-label="Nahaufnahme grüner Hanfblätter"></div>

  <div class="brand-box">
    <div class="brand-dot"></div>
    <div class="brand-name">TIROVELMO</div>
  </div>

  <div class="claim-band claim-band--origin">handgemacht in Österreich</div>

  <div class="veil-band"></div>
  <section class="product-label">
    <h1 class="product-title"><span>Hanf</span><span class="line-2">nudeln</span></h1>
    <p class="ingredients"><strong>Zutaten:</strong><br>Dinkel, Hanfmehl, Steinsalz,<br>nitratfreies Wasser</p>
    <div class="pack-info">
      <span>500g</span>
      <svg width="34" height="30" viewBox="0 0 34 30" aria-label="Kochzeit 3 Minuten">
        <rect x="12" y="0" width="10" height="4" rx="1" fill="#2b3a2a"/>
        <rect x="3" y="4" width="28" height="5" rx="2" fill="#2b3a2a"/>
        <rect x="0" y="10" width="34" height="4" rx="2" fill="#2b3a2a"/>
        <rect x="3" y="12" width="28" height="18" rx="2" fill="#2b3a2a"/>
        <text x="17" y="25" font-family="Open Sans, sans-serif" font-size="7" font-weight="700" fill="#fff" text-anchor="middle">3 Min.</text>
      </svg>
    </div>
  </section>

  <div class="claim-band claim-band--diet">100% Vegan | BIO</div>

  <div class="leaf-photo leaf-photo--bottom" role="img" aria-label="Unscharfe Nahaufnahme grüner Hanfblätter"></div>
</body>
</html>
```